Auto Detailing Facility Needs Facebook Cover Photo

Looking for a beautiful Facebook cover photo using our logo and a photo, including our business information. Does not have to use the photo provided but the logo must be in there. I want an eye-catching cover photo that promotes the luxury brand.

Website: www.glossbayauto.com
Phone: 508-555-0147
Address: 412 Lower Maple Rd Unit B-3 Franklin, MA 02091

Industry/Entity Type

Automotive

Colors

Designer to choose colors to be used in the design.

```html
<!DOCTYPE html>
<html lang="en">
<head>
<meta charset="utf-8">
<title>Gloss Bay Auto – Cover</title>
<link href="https://fonts.googleapis.com/css2?family=Montserrat:wght@300;400;500&display=swap" rel="stylesheet">
<style>
  :root {
    --page: #ffffff;
    --black: #000000;
    --green: #5bc236;
    --white: #ffffff;
    --wall: #161616;
  }
  html, body {
    margin: 0;
    width: 1200px;
    height: 1200px;
    overflow: hidden;
    background: var(--page);
    font-family: "Montserrat", sans-serif;
  }
  .cover {
    position: absolute;
    left: 151px;
    top: 397px;
    width: 908px;
    height: 345px;
    background: var(--black);
    overflow: hidden;
    box-shadow: 0 8px 18px rgba(0, 0, 0, 0.35);
  }
  .cover__art {
    position: absolute;
    inset: 0;
  }
  .brand {
    position: absolute;
    left: 69px;
    top: 82px;
    margin: 0;
    display: flex;
    align-items: center;
    gap: 10px;
    color: var(--white);
    font-weight: 300;
    font-size: 20px;
    letter-spacing: 1px;
  }
  .brand__mark {
    width: 14px;
    height: 14px;
    border-radius: 50%;
    background: var(--green);
    flex: none;
  }
  .contact {
    position: absolute;
    left: 28px;
    top: 197px;
    margin: 0;
    padding: 0;
    list-style: none;
  }
  .contact__item {
    display: flex;
    align-items: flex-start;
    color: var(--white);
  }
  .contact__icon {
    width: 24px;
    height: 24px;
    margin-right: 14px;
    flex: none;
  }
  .contact__phone {
    color: var(--green);
    font-size: 25px;
    font-weight: 400;
    line-height: 30px;
  }
  .contact__address {
    margin-top: 8px;
    font-size: 16px;
    line-height: 19px;
    font-weight: 400;
  }
  .contact__web {
    margin-top: 8px;
    font-size: 15px;
    letter-spacing: 3px;
    line-height: 24px;
  }
  .contact__web-domain { color: var(--green); }
</style>
</head>
<body>
  <section class="cover">
    <svg class="cover__art" width="908" height="345" viewBox="0 0 908 345">
      <defs>
        <radialGradient id="carTones" gradientUnits="userSpaceOnUse" cx="660" cy="225" r="300"
                        gradientTransform="translate(660 225) scale(1 0.55) translate(-660 -225)">
          <stop offset="0" stop-color="#7fd13f"/>
          <stop offset="0.35" stop-color="#5cb62b"/>
          <stop offset="0.6" stop-color="#2f6e18"/>
          <stop offset="0.82" stop-color="#17220f"/>
          <stop offset="1" stop-color="var(--wall)"/>
        </radialGradient>
      </defs>
      <polygon class="cover__photo" points="252,0 908,0 908,345 590,345"
               fill="url(#carTones)" role="img"
               aria-label="Photo of a green luxury sports car with headlights on, in front of a dark brick wall"/>
      <polygon class="cover__stripe" points="229,0 252,0 590,345 563,345" fill="var(--green)"/>
    </svg>

    <p class="brand"><span class="brand__mark"></span>GLOSS BAY AUTO</p>

    <ul class="contact">
      <li class="contact__item">
        <svg class="contact__icon" viewBox="0 0 24 24" fill="none" stroke="var(--green)" stroke-width="1.5" stroke-linejoin="round">
          <path d="M5 3l4 1 1 4-2 2c1 3 3 5 6 6l2-2 4 1 1 4-2 2C10 21 3 14 3 5z"/>
          <path d="M14 6a4 4 0 0 1 4 4M14 2a8 8 0 0 1 8 8"/>
        </svg>
        <span class="contact__phone">508-555-0147</span>
      </li>
      <li class="contact__item contact__address">
        <svg class="contact__icon" viewBox="0 0 24 24" fill="none" stroke="var(--green)" stroke-width="1.5">
          <path d="M12 22s-7-7-7-12a7 7 0 0 1 14 0c0 5-7 12-7 12z"/>
          <circle cx="12" cy="10" r="2.5"/>
        </svg>
        <span>412 Lower Maple Rd Unit B-3<br>Franklin, MA 02091</span>
      </li>
      <li class="contact__item contact__web">
        <svg class="contact__icon" viewBox="0 0 24 24">
          <rect x="1" y="5" width="22" height="14" fill="var(--green)"/>
          <path d="M1 5l11 8 11-8" fill="none" stroke="var(--black)" stroke-width="1.5"/>
        </svg>
        <span>www.<span class="contact__web-domain">glossbayauto</span>.com</span>
      </li>
    </ul>
  </section>
</body>
</html>
```